pressure washing advertisment

I would like front and back designed post cards. we offer pressure washing services for residential customers. I want to highlight before and after pictures as examples of our more popular services. I would also like to have our email www.brightlanewashco.com and the facebook and Instagram logo somewhere. you can also include all major credit card logos as acceptable payments. I have attached our logo along with before and after pictures. also feel free to go to my website for any additional information that should be added to the post card. lastly I want a small promotion of $25 off any service somewhere.<br/><br/>Thank you!!

Target Market(s)

homeowners

Industry/Entity Type

Cleaning Service

Font styles to use
Serif
Sans Serif

Colors

Designer to choose colors to be used in the design.

Requirements
Must have
• before and after pictures with website and logo
Nice to have
• clean look that flows

```html
<!DOCTYPE html>
<html lang="en">
<head>
<meta charset="utf-8">
<title>Bright Lane Wash Co – Postcards</title>
<link href="https://fonts.googleapis.com/css2?family=Figtree:ital,wght@0,400;0,600;0,700;1,600&family=Merriweather:ital,wght@0,400;1,400;1,700&display=swap" rel="stylesheet">
<style>
  :root {
    --bg: #3a3a3c;
    --card: #e6e6e6;
    --blue: #2b88d8;
    --navy: #1f3e9c;
    --red: #ee1a3e;
    --ink: #222222;
    --white: #ffffff;
  }
  * { box-sizing: border-box; margin: 0; padding: 0; }
  html, body { width: 1200px; height: 1200px; overflow: hidden; }
  body { background: var(--bg); position: relative; font-family: "Figtree", sans-serif; }

  .postcard {
    position: absolute; left: 239px; width: 722px; height: 481px;
    background: var(--card);
  }
  .postcard--front { top: 78px; }
  .postcard--back { top: 640px; }

  /* Brand */
  .brand { position: absolute; left: 45px; top: 46px; display: flex; align-items: center; gap: 8px; }
  .brand__dot { width: 18px; height: 18px; border-radius: 50%; background: var(--red); }
  .brand__name { font-weight: 700; font-size: 19px; color: var(--navy); letter-spacing: 0.3px; }

  /* Headline */
  .headline { position: absolute; left: 44px; top: 125px; color: var(--blue); }
  .headline__kicker { display: block; font-weight: 400; font-size: 42px; letter-spacing: 8px; line-height: 46px; }
  .headline__main { display: block; font-weight: 700; font-size: 72px; line-height: 57px; letter-spacing: -1px; margin-top: 2px; }
  .headline__main span { display: block; }

  /* Offer tag */
  .offer { position: absolute; left: 46px; top: 370px; width: 179px; height: 66px; filter: drop-shadow(2px 6px 5px rgba(0,0,0,0.35)); }
  .offer svg { position: absolute; inset: 0; }
  .offer__text { position: absolute; left: 0; right: 0; top: 12px; text-align: center; color: var(--white); font-family: "Merriweather", serif; font-style: italic; }
  .offer__amount { display: block; font-weight: 700; font-size: 26px; line-height: 26px; }
  .offer__note { display: block; font-size: 20px; line-height: 20px; }

  /* Service gallery */
  .service { position: absolute; left: 501px; width: 179px; text-align: center; }
  .service--house { top: 47px; }
  .service--drive { top: 179px; }
  .service--deck { top: 311px; }
  .service__photos { display: flex; gap: 3px; background: var(--white); padding: 3px; height: 99px; }
  .service__photo { flex: 1; }
  .service__label { font-family: "Merriweather", serif; font-size: 13.5px; line-height: 14px; color: var(--ink); margin-top: 4px; }

  .photo-house-before { background: linear-gradient(160deg, #d9d2a0 0%, #b7b07a 60%, #3c5a2c 100%); }
  .photo-house-after { background: linear-gradient(160deg, #5aa0e6 0%, #e9e2b4 40%, #cfc795 75%, #3f6a2e 100%); }
  .photo-drive-before { background: linear-gradient(180deg, #1f2e1a 0%, #2f4226 30%, #9a9c98 45%, #b5b6b2 100%); }
  .photo-drive-after { background: linear-gradient(180deg, #1f2e1a 0%, #354a2a 30%, #c3c5be 45%, #d6d7d0 100%); }
  .photo-deck-before { background: linear-gradient(135deg, #2d3a2a 0%, #55603f 50%, #28331f 100%); }
  .photo-deck-after { background: linear-gradient(135deg, #6a5520 0%, #9c8036 50%, #4c3a16 100%); }

  /* Back */
  .stamp-box { position: absolute; left: 598px; top: 54px; width: 72px; height: 72px; border: 1px solid var(--ink); }
  .cta { position: absolute; left: 52px; top: 210px; color: var(--blue); font-weight: 600; font-style: italic; font-size: 33px; line-height: 33px; letter-spacing: -0.8px; word-spacing: -2px; }
  .contacts { position: absolute; left: 53px; top: 331px; list-style: none; }
  .contacts li { display: flex; align-items: center; gap: 7px; font-family: "Merriweather", serif; font-style: italic; font-size: 13px; line-height: 15.5px; color: var(--blue); }
  .contacts svg { width: 12px; height: 12px; flex: none; }
  .rule { position: absolute; left: 53px; top: 411px; width: 24px; height: 2px; background: var(--navy); }
  .payment-title { position: absolute; left: 53px; top: 418px; font-family: "Merriweather", serif; font-style: italic; font-size: 7.5px; color: var(--navy); }
  .payment-cards { position: absolute; left: 53px; top: 434px; display: flex; gap: 2px; }
  .payment-card { width: 17px; height: 12px; border-radius: 1px; }
  .payment-card--a { background: #2f6fd8; }
  .payment-card--b { background: #f2f2f2; border: 1px solid #2f6fd8; }
  .payment-card--c { background: #cfe6f5; }
  .payment-card--d { background: #e9eef6; }
  .payment-card--e { background: #2a2a3a; }
  .payment-card--f { background: #3ea1e4; }
</style>
</head>
<body>

<section class="postcard postcard--front">
  <div class="brand">
    <span class="brand__dot"></span>
    <span class="brand__name">BRIGHT LANE WASH CO</span>
  </div>

  <h1 class="headline">
    <span class="headline__kicker">Residential</span>
    <span class="headline__main"><span>Pressure</span><span>Washing</span><span>Services</span></span>
  </h1>

  <div class="offer">
    <svg viewBox="0 0 179 66" width="179" height="66" preserveAspectRatio="none">
      <defs>
        <linearGradient id="tagFill" x1="0" y1="0" x2="0" y2="1">
          <stop offset="0" stop-color="#f53a5a"/>
          <stop offset="1" stop-color="#e00f30"/>
        </linearGradient>
      </defs>
      <path d="M0 14 Q60 0 89 0 Q118 0 179 14 L179 66 L0 66 Z" fill="url(#tagFill)"/>
      <circle cx="88" cy="7" r="3.5" fill="#c8c8c8"/>
    </svg>
    <div class="offer__text">
      <span class="offer__amount">25$ OFF</span>
      <span class="offer__note">on any service</span>
    </div>
  </div>

  <div class="service service--house">
    <div class="service__photos">
      <div class="service__photo photo-house-before" role="img" aria-label="Before photo: house siding before soft washing"></div>
      <div class="service__photo photo-house-after" role="img" aria-label="After photo: house siding after soft washing"></div>
    </div>
    <p class="service__label">Soft Wash House<br>Washing</p>
  </div>

  <div class="service service--drive">
    <div class="service__photos">
      <div class="service__photo photo-drive-before" role="img" aria-label="Before photo: stained concrete driveway"></div>
      <div class="service__photo photo-drive-after" role="img" aria-label="After photo: clean concrete driveway"></div>
    </div>
    <p class="service__label">Driveway &amp;<br>Concrete Cleaning</p>
  </div>

  <div class="service service--deck">
    <div class="service__photos">
      <div class="service__photo photo-deck-before" role="img" aria-label="Before photo: weathered wooden deck"></div>
      <div class="service__photo photo-deck-after" role="img" aria-label="After photo: cleaned wooden deck"></div>
    </div>
    <p class="service__label">Deck &amp; Fence<br>Cleaning</p>
  </div>
</section>

<section class="postcard postcard--back">
  <div class="stamp-box"></div>

  <h2 class="cta">Contact us today to<br>schedule your next<br>cleaning service.</h2>

  <ul class="contacts">
    <li>
      <svg viewBox="0 0 12 12"><circle cx="6" cy="6" r="6" fill="#2b88d8"/><path d="M4 3.2 L5 3 L5.6 4.5 L5 5 Q5.6 6.4 7 7 L7.5 6.4 L9 7 L8.8 8 Q6.8 8.6 5 7 Q3.4 5.2 4 3.2 Z" fill="#fff"/></svg>
      (555) 201-4837
    </li>
    <li>
      <svg viewBox="0 0 12 12"><circle cx="6" cy="6" r="6" fill="#2b88d8"/><circle cx="6" cy="6" r="3.6" fill="none" stroke="#fff" stroke-width="0.8"/><path d="M2.4 6 H9.6 M6 2.4 V9.6" stroke="#fff" stroke-width="0.8"/></svg>
      www.brightlanewashco.com
    </li>
    <li>
      <svg viewBox="0 0 12 12"><circle cx="6" cy="6" r="6" fill="#2b88d8"/></svg>
      photos/brightlanewash
    </li>
    <li>
      <svg viewBox="0 0 12 12"><circle cx="6" cy="6" r="6" fill="#2b88d8"/></svg>
      page/BrightLaneWash
    </li>
  </ul>

  <div class="rule"></div>
  <p class="payment-title">Payment Acceptable:</p>
  <div class="payment-cards">
    <span class="payment-card payment-card--a"></span>
    <span class="payment-card payment-card--b"></span>
    <span class="payment-card payment-card--c"></span>
    <span class="payment-card payment-card--d"></span>
    <span class="payment-card payment-card--e"></span>
    <span class="payment-card payment-card--f"></span>
  </div>
</section>

</body>
</html>
```